Letterhead and Business card for Construction company

We need a letterhead and business card with our new company logo. We are based in NY. We develop and build properties.

The design should incorporate some unique feature from the logo (shape, font...). it should look like an extension from it.

Design should be clean and elegant, professional, not too busy.

The letterhead should include:
Logo (attached)
Address
Phone
Email

Please find the attached logo images and AI file.

Target Market(s)

Construction industry professionals

Industry/Entity Type

Construction, Development

Font styles to use
Sans Serif

Colors

Designer to choose colors to be used in the design.

Requirements
Must have
• Design should incorporate logo elements, additional assets are welcome. I'd like to see some other shapes / images invorporated too.

```html
<!DOCTYPE html>
<html lang="en">
<head>
<meta charset="utf-8">
<title>Halvern Builders Letterhead</title>
<link rel="stylesheet" href="https://fonts.googleapis.com/css2?family=Saira:wght@400;700&display=swap">
<style>
  :root {
    --paper: #ffffff;
    --charcoal: #2a2826;
    --orange: #ee7b1e;
    --band-grey: #dadcdb;
    --ghost: #f4f5f5;
    --text: #2d2d2d;
  }
  html, body {
    margin: 0;
    padding: 0;
    width: 899px;
    height: 1200px;
    overflow: hidden;
    background: var(--paper);
  }
  .letterhead {
    position: relative;
    width: 899px;
    height: 1200px;
    overflow: hidden;
    background: var(--paper);
    font-family: "Saira", sans-serif;
    color: var(--text);
  }
  .side-band {
    position: absolute;
    left: 38px;
    top: 0;
    width: 43px;
    height: 1200px;
    background: var(--band-grey);
  }
  .corner-accents {
    position: absolute;
    left: 0;
    top: 0;
    width: 100px;
    height: 200px;
  }
  .brand-mark {
    position: absolute;
    left: 120px;
    top: 52px;
    width: 12px;
    height: 12px;
    background: var(--orange);
  }
  .brand-name {
    position: absolute;
    left: 120px;
    top: 70px;
    margin: 0;
    font-weight: 700;
    font-size: 30px;
    line-height: 31px;
    letter-spacing: 0.5px;
    text-transform: uppercase;
    color: var(--charcoal);
  }
  .ghost-name {
    position: absolute;
    right: 12px;
    top: 600px;
    margin: 0;
    font-weight: 700;
    font-size: 64px;
    line-height: 1;
    text-transform: uppercase;
    color: var(--ghost);
    white-space: nowrap;
  }
  .contact-bar {
    position: absolute;
    top: 1146px;
    left: 0;
    width: 100%;
    height: 24px;
  }
  .contact-item {
    position: absolute;
    top: 0;
    display: flex;
    align-items: center;
    gap: 11px;
    font-size: 16px;
    line-height: 24px;
    letter-spacing: 0.3px;
    white-space: nowrap;
  }
  .contact-item.phone { left: 136px; }
  .contact-item.email { left: 316px; }
  .contact-item.address { left: 573px; }
  .contact-icon {
    width: 16px;
    height: 16px;
    flex: none;
  }
</style>
</head>
<body>
<main class="letterhead">
  <div class="side-band" aria-hidden="true"></div>
  <svg class="corner-accents" viewBox="0 0 100 200" aria-hidden="true">
    <rect class="accent-block" x="0" y="0" width="38" height="26" fill="var(--charcoal)"/>
    <rect class="accent-bar" x="0" y="44" width="94" height="14" fill="var(--orange)"/>
    <rect class="accent-bar-thin" x="0" y="72" width="38" height="6" fill="var(--charcoal)"/>
  </svg>

  <span class="brand-mark" aria-hidden="true"></span>
  <h1 class="brand-name">Halvern<br>Builders</h1>

  <p class="ghost-name" aria-hidden="true">Halvern</p>

  <footer class="contact-bar">
    <div class="contact-item phone">
      <svg class="contact-icon" viewBox="0 0 16 16" aria-hidden="true">
        <rect width="16" height="16" rx="3" fill="var(--orange)"/>
        <path d="M5 3.5l1.6 0 .8 2.3-1.1.8a6 6 0 0 0 3.1 3.1l.8-1.1 2.3.8 0 1.6c0 .6-.5 1-1 1A8 8 0 0 1 4 4.5c0-.5.4-1 1-1z" fill="#fff"/>
      </svg>
      <span>(000) 234 5678</span>
    </div>
    <div class="contact-item email">
      <svg class="contact-icon" viewBox="0 0 16 16" aria-hidden="true">
        <rect width="16" height="16" rx="3" fill="var(--orange)"/>
        <rect x="3.5" y="5" width="9" height="6.5" fill="none" stroke="#fff" stroke-width="1.2"/>
        <path d="M3.5 5l4.5 3.6L12.5 5" fill="none" stroke="#fff" stroke-width="1.2"/>
      </svg>
      <span>office@halvernbuilders.com</span>
    </div>
    <div class="contact-item address">
      <svg class="contact-icon" viewBox="0 0 16 16" aria-hidden="true">
        <rect width="16" height="16" rx="3" fill="var(--orange)"/>
        <path d="M8 3a3 3 0 0 1 3 3c0 2.2-3 5.5-3 5.5S5 8.2 5 6a3 3 0 0 1 3-3z" fill="none" stroke="#fff" stroke-width="1.2"/>
        <circle cx="8" cy="6" r="1" fill="#fff"/>
        <path d="M4 13h8" stroke="#fff" stroke-width="1.2"/>
      </svg>
      <span>Name, Street no., area, city pincode</span>
    </div>
  </footer>
</main>
</body>
</html>
```